My website design

It Will be a to-go website for all service requests from the comfort of your home. services ranging from renting an electrician to fix your home electrical issues, DJ for your party, mark-up artist for your wedding and so on. Here are a few websites for inspiration:

https://www.dwellpanel.example/
https://www.chorewren.example/
https://www.gigplover.example/

Number of Pages Required

5+ page

Requirements
Must have
• User's registration form
pros resgistation form
filling out job request form
quotes sent sent back to job requester from various pros within the same zip code
quote accepted
ability to review pros once jobs are completed

```html
<!DOCTYPE html>
<html lang="en">
<head>
<meta charset="utf-8">
<title>Tarvoly – Find trusted local pros</title>
<link href="https://fonts.googleapis.com/css2?family=Poppins:wght@400;500;600&display=swap" rel="stylesheet">
<style>
:root{
  --green:#3ab54a;
  --green-soft:#dff6e1;
  --slate:#5e6f7b;
  --slate-dark:#4f5f6a;
  --ink:#1f1f1f;
  --muted:#555;
  --light:#f7f7f9;
  --lilac:#f9f7fb;
  --white:#fff;
}
*{box-sizing:border-box;margin:0;padding:0}
html,body{width:1200px;height:2625px;overflow:hidden}
body{font-family:'Poppins',sans-serif;color:var(--ink);background:var(--white)}
.page{position:relative;width:1200px;height:2625px;overflow:hidden}
.abs{position:absolute}
a{color:inherit;text-decoration:none}

/* header */
.brand{left:85px;top:30px;display:flex;align-items:center;gap:12px;font-size:24px;font-weight:500;letter-spacing:9px;color:var(--slate);text-transform:uppercase;white-space:nowrap}
.brand-mark{width:26px;height:26px;background:var(--green)}
.btn{background:var(--green);color:var(--white);font-weight:600;font-size:12px;display:flex;align-items:center;justify-content:center;border-radius:2px;white-space:nowrap}
.join{left:784px;top:31px;width:126px;height:38px}
.nav-link{top:41px;font-size:12px;font-weight:500;color:var(--slate);white-space:nowrap}

/* hero */
.hero{left:0;top:97px;width:1200px;height:390px;background:linear-gradient(180deg,#7a8891 0%,#6b7a85 50%,#5f6e79 100%)}
.hero h1{position:absolute;top:154px;width:100%;text-align:center;font-size:31px;font-weight:500;color:var(--white)}
.search{left:296px;top:319px;width:607px;height:55px;background:rgba(255,255,255,.35);padding:5px;display:flex}
.search-input{flex:1;background:var(--white);font-size:12px;color:#888;display:flex;align-items:center;padding-left:16px}
.search-btn{width:139px;font-size:13px}
.covid{top:422px;width:100%;display:flex;justify-content:center;align-items:center;gap:8px;font-size:10.5px;color:var(--white)}
.covid b{font-weight:600}

/* section titles */
.section-title{width:100%;text-align:center;font-size:24px;font-weight:500}
.rule{width:44px;height:2px;background:var(--green);left:578px}

/* photo cards */
.card{overflow:hidden}
.card .label{position:absolute;left:0;right:0;bottom:0;padding:0 0 22px;text-align:center;color:var(--white);background:linear-gradient(180deg,transparent,rgba(0,0,0,.85));height:90px;display:flex;flex-direction:column;justify-content:flex-end}
.card .label strong{font-size:15px;font-weight:500}
.card .label span{font-size:11.5px;font-weight:600;margin-top:6px;display:flex;justify-content:center;align-items:center;gap:6px}
.viewmore{left:538px;top:886px;width:124px;height:39px}

/* app band */
.appband{left:0;top:989px;width:1200px;height:171px;background:var(--slate)}
.phone{left:320px;top:963px;width:133px;height:197px;background:linear-gradient(180deg,#fdfdfd 0%,#e9ecef 45%,#cfd5da 100%);border:3px solid #f2f2f2;border-bottom:none;border-radius:16px 16px 0 0}
.app-title{left:514px;top:1036px;font-size:21px;font-weight:500;color:var(--white);white-space:nowrap}
.store{top:1078px;height:32px;display:flex;align-items:center;gap:10px;padding-left:12px;color:var(--white);font-size:9.5px;line-height:1.1}
.store small{font-size:7px;display:block}
.store-a{left:514px;width:117px;background:#8b98a1}
.store-b{left:641px;width:115px;background:var(--green)}

/* categories */
.cats{left:0;top:1160px;width:1200px;height:541px;background:var(--light)}
.tab{top:1237px;font-size:15px;font-weight:600;white-space:nowrap}
.tab.active{color:var(--green);border-bottom:2px solid var(--green);padding-bottom:6px}
.card.small .label{text-align:left;padding-left:26px;height:80px;padding-bottom:18px}
.card.small .label span{justify-content:flex-start;font-weight:400;font-size:10px}

/* trending */
.pills{top:1856px;width:100%;display:flex;justify-content:center;gap:6px}
.pill{background:var(--green-soft);border-radius:12px;font-size:10px;font-weight:500;height:22px;padding:0 12px;display:flex;align-items:center;color:#2d3a2f;white-space:nowrap}

/* cities */
.cities{left:0;top:1948px;width:1200px;height:311px;background:var(--lilac)}
.cities-head{left:235px;top:1995px;display:flex;align-items:center;gap:16px;font-size:15px;font-weight:500;white-space:nowrap}
.cities-head .sep{width:1px;height:14px;background:#ccc}
.cities-head .browse{color:var(--green);font-weight:400}
.city-col{top:2045px;font-size:10.5px;line-height:26.3px;color:var(--ink);list-style:none;white-space:nowrap}
.more{left:235px;top:2190px;font-size:11px;color:var(--green)}

/* footer */
.footer{left:0;top:2259px;width:1200px;height:366px;background:var(--slate)}
.foot-col{top:2304px;color:var(--white);list-style:none;white-space:nowrap}
.foot-col h4{font-size:15px;font-weight:500;margin-bottom:18px}
.foot-col li{font-size:10.5px;line-height:26.3px}
.socials{left:235px;top:2468px;display:flex;gap:4px}
.socials span{width:20px;height:20px;border:1px solid var(--white);border-radius:50%}
.divider{left:235px;top:2566px;width:730px;height:1px;background:#7b8a94}
.copy{top:2591px;width:100%;text-align:center;font-size:9px;color:var(--white)}
</style>
</head>
<body>
<div class="page">

  <!-- Header -->
  <div class="abs brand"><span class="brand-mark"></span>Tarvoly</div>
  <a class="abs btn join" href="#">Join as a pro</a>
  <a class="abs nav-link" style="left:941px" href="#">Explore</a>
  <a class="abs nav-link" style="left:1014px" href="#">Sign Up</a>
  <a class="abs nav-link" style="left:1084px" href="#">Log in</a>

  <!-- Hero -->
  <section class="abs hero" role="img" aria-label="Electrician with tool belt and coiled cable, muted blue-grey overlay">
    <h1>Find trusted local pros for any home project.</h1>
  </section>
  <div class="abs search">
    <div class="search-input">What service do you need?</div>
    <div class="btn search-btn">Find Pros</div>
  </div>
  <p class="abs covid">
    <svg width="14" height="14" viewBox="0 0 14 14"><circle cx="7" cy="7" r="7" fill="#fff"/><rect x="6.2" y="6" width="1.6" height="5" fill="#6b7a85"/><circle cx="7" cy="3.8" r="1" fill="#6b7a85"/></svg>
    A note about home projects during Coronavirus (COVID-19). <b>Learn More</b>
  </p>

  <!-- Popular projects -->
  <h2 class="abs section-title" style="top:550px">Popular projects in your area</h2>
  <div class="abs rule" style="top:598px"></div>

  <div class="abs card" style="left:234px;top:644px;width:232px;height:199px;background:linear-gradient(135deg,#6d6a62,#a58f6e 50%,#3a3935)" role="img" aria-label="Electrician working on a wiring panel">
    <div class="label"><strong>Electrician</strong><span><svg width="12" height="12" viewBox="0 0 12 12"><path d="M0 6L6 0h6v6l-6 6z" fill="#fff"/><circle cx="9" cy="3" r="1.2" fill="#333"/></svg>Avg. Project: $55 – $144</span></div>
  </div>
  <div class="abs card" style="left:484px;top:644px;width:232px;height:199px;background:linear-gradient(135deg,#1c2a6b,#2f4fb0 50%,#0d1330)" role="img" aria-label="DJ mixing deck under blue light">
    <div class="label"><strong>DJ Party</strong><span><svg width="12" height="12" viewBox="0 0 12 12"><path d="M0 6L6 0h6v6l-6 6z" fill="#fff"/><circle cx="9" cy="3" r="1.2" fill="#333"/></svg>Avg. Project: $55 – $144</span></div>
  </div>
  <div class="abs card" style="left:734px;top:644px;width:232px;height:199px;background:linear-gradient(135deg,#5a3e2e,#c9a17a 50%,#3a2a22)" role="img" aria-label="Bride having wedding makeup applied">
    <div class="label"><strong>Wedding Makeup Artist</strong><span><svg width="12" height="12" viewBox="0 0 12 12"><path d="M0 6L6 0h6v6l-6 6z" fill="#fff"/><circle cx="9" cy="3" r="1.2" fill="#333"/></svg>Avg. Project: $55 – $144</span></div>
  </div>
  <a class="abs btn viewmore" href="#">View More</a>

  <!-- App band -->
  <section class="abs appband"></section>
  <div class="abs phone" role="img" aria-label="Phone showing the Tarvoly mobile home screen"></div>
  <h2 class="abs app-title">Download our award-winning app.</h2>
  <a class="abs store store-a" href="#"><svg width="16" height="16" viewBox="0 0 16 16"><rect x="2" y="2" width="12" height="12" rx="3" fill="#fff"/></svg><span><small>Available on the</small>AppBay</span></a>
  <a class="abs store store-b" href="#"><svg width="16" height="16" viewBox="0 0 16 16"><rect x="2" y="2" width="12" height="12" rx="3" fill="#fff"/></svg><span><small>Available on the</small>PlayDock</span></a>

  <!-- Categories -->
  <section class="abs cats"></section>
  <span class="abs tab active" style="left:427px">Home Maintenance</span>
  <span class="abs tab" style="left:603px">DJ Party</span>
  <span class="abs tab" style="left:695px">Weddings</span>

  <div class="abs card small" style="left:234px;top:1311px;width:232px;height:312px;background:linear-gradient(160deg,#e6e6e6,#36508a 55%,#1e2b4a)" role="img" aria-label="Electrician testing wires with a multimeter">
    <div class="label"><strong>Electrician</strong><span><svg width="10" height="12" viewBox="0 0 10 12"><path d="M5 0a5 5 0 0 1 5 5c0 3-5 7-5 7S0 8 0 5a5 5 0 0 1 5-5z" fill="#fff"/><circle cx="5" cy="5" r="1.8" fill="#333"/></svg>See pros near you</span></div>
  </div>
  <div class="abs card small" style="left:484px;top:1311px;width:232px;height:148px;background:linear-gradient(160deg,#cfcfcf,#6d6d6d 50%,#222)" role="img" aria-label="Hands stripping electrical cable">
    <div class="label"><strong>Electrician</strong><span><svg width="10" height="12" viewBox="0 0 10 12"><path d="M5 0a5 5 0 0 1 5 5c0 3-5 7-5 7S0 8 0 5a5 5 0 0 1 5-5z" fill="#fff"/><circle cx="5" cy="5" r="1.8" fill="#333"/></svg>See pros near you</span></div>
  </div>
  <div class="abs card small" style="left:484px;top:1476px;width:232px;height:147px;background:linear-gradient(160deg,#d9dde3,#4f6fa6 55%,#1a2340)" role="img" aria-label="Electrician in hard hat at a fuse board">
    <div class="label"><strong>Electrician</strong><span><svg width="10" height="12" viewBox="0 0 10 12"><path d="M5 0a5 5 0 0 1 5 5c0 3-5 7-5 7S0 8 0 5a5 5 0 0 1 5-5z" fill="#fff"/><circle cx="5" cy="5" r="1.8" fill="#333"/></svg>See pros near you</span></div>
  </div>
  <div class="abs card small" style="left:734px;top:1311px;width:232px;height:312px;background:linear-gradient(160deg,#e9e4dc,#b59a80 50%,#2c3550)" role="img" aria-label="Electrician showing a customer a fuse box">
    <div class="label"><strong>Electrician</strong><span><svg width="10" height="12" viewBox="0 0 10 12"><path d="M5 0a5 5 0 0 1 5 5c0 3-5 7-5 7S0 8 0 5a5 5 0 0 1 5-5z" fill="#fff"/><circle cx="5" cy="5" r="1.8" fill="#333"/></svg>See pros near you</span></div>
  </div>

  <!-- Trending -->
  <h2 class="abs section-title" style="top:1762px">Trending now in these areas.</h2>
  <div class="abs rule" style="top:1810px"></div>
  <div class="abs pills">
    <span class="pill">Atlanta</span><span class="pill">Boston</span><span class="pill">Dallas</span><span class="pill">Denver</span><span class="pill">Houston</span><span class="pill">Miami</span><span class="pill">Phoenix</span><span class="pill">San Francisco</span><span class="pill">Seattle</span><span class="pill">Washington DC</span>
  </div>

  <!-- Cities -->
  <section class="abs cities"></section>
  <div class="abs cities-head"><span>Most Popular Cities</span><span class="sep"></span><span class="browse">Browse by State &nbsp;›</span></div>
  <ul class="abs city-col" style="left:235px"><li>Atlanta, GA</li><li>Charlotte, NC</li><li>Chicago, IL</li><li>Dallas, TX</li><li>Denver, CO</li></ul>
  <ul class="abs city-col" style="left:386px"><li>Houston, TX</li><li>Los Angeles, CA</li><li>Miami, FL</li><li>Milwaukee, WI</li><li>Minneapolis, MN</li></ul>
  <ul class="abs city-col" style="left:537px"><li>New Orleans, LA</li><li>New York, NY</li><li>Philadelphia, PA</li><li>Portland, OR</li><li>Salt Lake City, UT</li></ul>
  <ul class="abs city-col" style="left:693px"><li>San Antonio, TX</li><li>San Diego, CA</li><li>San Francisco, CA</li><li>Seattle, WA</li><li>Washington, DC</li></ul>
  <ul class="abs city-col" style="left:833px"><li>Oklahoma</li><li>Oregon</li><li>Pennsylvania</li><li>Rhode Island</li><li>South Carolina</li></ul>
  <a class="abs more" href="#">Additional Cities +</a>

  <!-- Footer -->
  <footer class="abs footer"></footer>
  <ul class="abs foot-col" style="left:235px"><h4>Information</h4><li>About</li><li>Careers</li><li>Press</li><li>Blog</li></ul>
  <div class="abs socials"><span></span><span></span><span></span><span></span></div>
  <ul class="abs foot-col" style="left:404px"><h4>Customers</h4><li>How to use Tarvoly</li><li>Sign up</li><li>Get the app</li><li>Services near me</li><li>Cost estimates</li><li>Project how to's</li><li>Project guides</li></ul>
  <ul class="abs foot-col" style="left:598px"><h4>Pros</h4><li>Tarvoly for pros</li><li>Sign up as a pro</li><li>Community</li><li>Success stories</li><li>Pro reviews</li><li>Pocketphone app for pros</li><li>Robodroid app for pros</li></ul>
  <ul class="abs foot-col" style="left:798px"><h4>Support</h4><li>Help</li><li>Safety</li><li>COVID-19 Info</li><li>Terms of Use</li><li>Privacy Policy</li><li>Do Not Sell My Info</li></ul>
  <div class="abs divider"></div>
  <p class="abs copy">© Copyright 2020 Tarvoly, Inc. All Rights Reserved</p>

</div>
</body>
</html>
```